Business Card for: Keelwright Financial Advisory Services Inc.

provide strategic financial advisory services to companies in the areas of corporate finance, mergers and acquisitions, executive coaching and strategic planning

Target Market(s)

Companies, banks, accountants, lawyers

Industry/Entity Type

High end business consulting in corporate finance, mergers and acquisitions, consulting

Contact Information for Business Card

Name of company, Name: xxxxxx xxxxxx , CEO, - phone number: 1-xxx-xxx-xxxx, - email address,

Requirements
Must have
• Must be professional and simple.
Nice to have
• simple, straight graphics, must give the impression that we are trustworthy, professional, competent
Should not have
• loud colors, loud design features

```html
<!DOCTYPE html>
<html lang="en">
<head>
<meta charset="utf-8">
<title>Keelwright Financial Advisory Services Inc. — Business Card</title>
<link rel="stylesheet" href="https://fonts.googleapis.com/css2?family=Lexend:wght@300;400;600&display=swap">
<style>
  :root {
    --navy: #221f63;
    --green: #45b864;
    --ink: #3a3a44;
    --paper: #ffffff;
    --backdrop: #d9d9d6;
    --ghost: #f3f3f8;
  }
  * { box-sizing: border-box; margin: 0; padding: 0; }
  html, body {
    width: 1200px; height: 850px; overflow: hidden;
    background: var(--backdrop);
    font-family: "Lexend", sans-serif;
  }
  .stage {
    width: 1200px; height: 850px;
    display: flex; flex-direction: column;
    align-items: center; justify-content: center; gap: 50px;
  }
  .card {
    position: relative;
    width: 630px; height: 360px;
    overflow: hidden;
    box-shadow: 0 6px 18px rgba(0,0,0,0.12);
  }

  /* Front */
  .card--front { background: var(--paper); }
  .card__ghost-circle {
    position: absolute; right: -90px; top: -110px;
    width: 320px; height: 320px; border-radius: 50%;
    border: 46px solid var(--ghost);
  }
  .brand {
    position: absolute; left: 40px; top: 62px;
    display: flex; align-items: center; gap: 12px;
    color: var(--navy); font-weight: 600;
  }
  .brand__dot {
    width: 14px; height: 14px; border-radius: 50%;
    background: var(--green); flex: none;
  }
  .brand__name { line-height: 1.1; }
  .brand__line1 { display: block; font-size: 27px; letter-spacing: -0.3px; }
  .brand__line2 { display: block; font-size: 12.5px; letter-spacing: 0.4px; }

  .contact {
    position: absolute; left: 40px; bottom: 50px;
  }
  .contact__name { color: var(--navy); font-weight: 600; font-size: 21px; }
  .contact__role { color: var(--green); font-weight: 400; font-size: 15px; margin-top: 2px; }
  .contact__list { list-style: none; margin-top: 18px; }
  .contact__item {
    display: flex; align-items: center; gap: 12px;
    color: var(--ink); font-weight: 300; font-size: 15px;
    margin-top: 6px;
  }
  .contact__icon { width: 15px; height: 15px; flex: none; }

  /* Back */
  .card--back {
    background: var(--navy);
    display: flex; align-items: center; justify-content: center;
  }
  .back-brand { color: var(--green); font-weight: 600; line-height: 1; }
  .back-brand__line1 { display: block; font-size: 64px; letter-spacing: -1px; }
  .back-brand__line2 { display: block; font-size: 54px; letter-spacing: -0.5px; margin-top: 4px; }
  .back-brand__line3 { display: block; font-size: 23px; letter-spacing: 0.6px; margin-top: 8px; }
</style>
</head>
<body>
<main class="stage">

  <section class="card card--front" aria-label="Business card front">
    <div class="card__ghost-circle" aria-hidden="true"></div>

    <div class="brand">
      <span class="brand__dot" aria-hidden="true"></span>
      <span class="brand__name">
        <span class="brand__line1">Keelwright Financial</span>
        <span class="brand__line2">Advisory Services Inc.</span>
      </span>
    </div>

    <div class="contact">
      <p class="contact__name">Daniel Ashcombe</p>
      <p class="contact__role">CEO</p>
      <ul class="contact__list">
        <li class="contact__item">
          <svg class="contact__icon" viewBox="0 0 24 24" aria-hidden="true">
            <path fill="var(--green)" d="M6.6 10.8a15.1 15.1 0 0 0 6.6 6.6l2.2-2.2a1 1 0 0 1 1-.25 11.4 11.4 0 0 0 3.6.57 1 1 0 0 1 1 1V20a1 1 0 0 1-1 1A17 17 0 0 1 3 4a1 1 0 0 1 1-1h3.5a1 1 0 0 1 1 1c0 1.25.2 2.45.57 3.6a1 1 0 0 1-.25 1z"/>
          </svg>
          (555) 214-0387
        </li>
        <li class="contact__item">
          <svg class="contact__icon" viewBox="0 0 24 24" aria-hidden="true">
            <path fill="var(--green)" d="M2 5h20v14H2z M2 5l10 8 10-8" stroke="var(--paper)" stroke-width="1.6" stroke-linejoin="round"/>
          </svg>
          daniel@keelwrightfinancial.com
        </li>
      </ul>
    </div>
  </section>

  <section class="card card--back" aria-label="Business card back">
    <p class="back-brand">
      <span class="back-brand__line1">Keelwright</span>
      <span class="back-brand__line2">Financial</span>
      <span class="back-brand__line3">Advisory Services Inc.</span>
    </p>
  </section>

</main>
</body>
</html>
```